Flyer Design for an electrical and security company trying to build local customers

I need a flyer design for a new company based in Sans Souci, Sydney 2219 called "Harbor Quill Dune Electrical and Security" also "HQD Electrical and Security". We are electrical contractors who are looking for more local work including emergency service calls and any project work including renovations or new constructions in the local area. I would like everyone in the area to know I am new and that I am available 24 hours a day 7 days a week. I would like to see designs that use the logo colours. Would also like the font of the entire design to be "juice bold".

Electrical

• juice bold

Requirements
Must have
• Must use the colours of the original logo and also have the information from the rear of the card. Must also have services buttons like the website picture attached.

```html
<!DOCTYPE html>
<html lang="en">
<head>
<meta charset="utf-8">
<title>Our Services</title>
<link rel="stylesheet" href="https://fonts.googleapis.com/css2?family=Jura:wght@600;700&display=swap">
<style>
  :root {
    --sky: #6fc0e3;
    --charcoal: #524a46;
    --ink: #3a3634;
    --coral: #f0855a;
    --white: #ffffff;
  }
  html, body {
    margin: 0;
    padding: 0;
    width: 1200px;
    height: 849px;
    overflow: hidden;
    background: var(--sky);
  }
  .flyer {
    position: relative;
    width: 1200px;
    height: 849px;
    background: var(--sky);
    font-family: "Jura", sans-serif;
    overflow: hidden;
  }
  .top-band {
    position: absolute;
    left: 0; top: 0;
    width: 100%; height: 33px;
    background: var(--charcoal);
  }
  .bottom-band {
    position: absolute;
    left: 0; bottom: 0;
    width: 100%; height: 34px;
    background: var(--coral);
  }
  .services-title {
    position: absolute;
    top: 76px;
    left: 0; width: 100%;
    margin: 0;
    padding-left: 12px;
    box-sizing: border-box;
    text-align: center;
    color: var(--white);
    font-size: 38px;
    font-weight: 700;
    letter-spacing: 1px;
  }
  .icons {
    position: absolute;
    left: 0; top: 0;
  }
  .badge { stroke: var(--ink); stroke-width: 1.5; }
  .badge-light { fill: var(--white); }
  .badge-accent { fill: var(--coral); }
  .glyph-dark { color: var(--ink); }
  .glyph-light { color: var(--white); }
  .cut-accent { fill: var(--coral); }
  .cut-white { fill: var(--white); }
  .service-label {
    position: absolute;
    width: 220px;
    margin-left: -110px;
    text-align: center;
    color: var(--ink);
    font-size: 26px;
    font-weight: 700;
    line-height: 29px;
    letter-spacing: 0.4px;
  }
</style>
</head>
<body>
<main class="flyer">
  <div class="top-band"></div>
  <h1 class="services-title">Our Servies</h1>

  <svg class="icons" width="1200" height="849" viewBox="0 0 1200 849" aria-hidden="true">
    <!-- row one -->
    <g transform="translate(237,222)">
      <circle class="badge badge-light" r="41"/>
      <g class="glyph-dark">
        <text x="0" y="7" font-family="Jura, sans-serif" font-weight="700" font-size="18" text-anchor="middle" fill="currentColor">24</text>
        <path d="M-22 2 A22 22 0 0 1 16 -15" fill="none" stroke="currentColor" stroke-width="2.5"/>
        <path d="M13 -22 L23 -13 L11 -10 Z" fill="currentColor"/>
        <path d="M22 4 A22 22 0 0 1 -18 13" fill="none" stroke="currentColor" stroke-width="2.5" stroke-dasharray="2 3"/>
      </g>
    </g>
    <g transform="translate(440,222)">
      <circle class="badge badge-accent" r="41"/>
      <g class="glyph-light">
        <g stroke="currentColor" stroke-width="5" stroke-linecap="round">
          <line x1="0" y1="-20" x2="0" y2="8"/>
          <line x1="-14" y1="-6" x2="14" y2="-6"/>
          <line x1="-10" y1="-16" x2="10" y2="4"/>
          <line x1="10" y1="-16" x2="-10" y2="4"/>
        </g>
        <circle cy="-6" r="10" fill="currentColor"/>
        <circle cy="-6" r="4" class="cut-accent"/>
        <path d="M-20 8 V18 H20 V8" fill="none" stroke="currentColor" stroke-width="3"/>
      </g>
    </g>
    <g transform="translate(627,222)">
      <circle class="badge badge-light" r="41"/>
      <g class="glyph-dark" fill="currentColor">
        <path d="M-12 -10 A12 12 0 0 1 12 -10 Z"/>
        <rect x="-14" y="-10" width="28" height="3"/>
        <circle cy="-1" r="8"/>
        <path d="M-20 22 V14 Q-20 8 -12 7 H12 Q20 8 20 14 V22 Z"/>
        <rect x="16" y="-10" width="4" height="22" rx="1"/>
        <path d="M13 -16 h10 v6 h-10 z"/>
      </g>
    </g>
    <g transform="translate(815,222)">
      <circle class="badge badge-accent" r="41"/>
      <g class="glyph-light">
        <g stroke="currentColor" stroke-width="5" stroke-linecap="round">
          <line x1="-14" y1="-14" x2="16" y2="16"/>
          <line x1="14" y1="-14" x2="-16" y2="16"/>
        </g>
        <circle cx="-16" cy="-16" r="5" fill="currentColor"/>
        <circle cx="17" cy="-17" r="6" fill="currentColor"/>
      </g>
    </g>
    <g transform="translate(1008,222)">
      <circle class="badge badge-light" r="41"/>
      <g class="glyph-dark">
        <path d="M-24 -2 L-6 -18 L12 -2" fill="none" stroke="currentColor" stroke-width="4"/>
        <rect x="-19" y="-2" width="26" height="22" fill="currentColor"/>
        <rect x="-14" y="2" width="6" height="6" class="cut-white"/>
        <rect x="-4" y="2" width="6" height="6" class="cut-white"/>
        <rect x="-10" y="11" width="7" height="9" class="cut-white"/>
        <line x1="20" y1="20" x2="20" y2="-14" stroke="currentColor" stroke-width="4"/>
        <path d="M13 -12 L20 -22 L27 -12 Z" fill="currentColor"/>
      </g>
    </g>

    <!-- row two -->
    <g transform="translate(237,448)">
      <circle class="badge badge-accent" r="41"/>
      <g class="glyph-light">
        <line x1="0" y1="-20" x2="0" y2="18" stroke="currentColor" stroke-width="3.5"/>
        <path d="M-5 -18 L0 -25 L5 -18 Z" fill="currentColor"/>
        <path d="M0 10 L-12 2 V-6" fill="none" stroke="currentColor" stroke-width="3"/>
        <path d="M0 4 L11 -3 V-9" fill="none" stroke="currentColor" stroke-width="3"/>
        <circle cx="-12" cy="-8" r="3.5" fill="currentColor"/>
        <rect x="8" y="-13" width="6" height="6" fill="currentColor"/>
        <circle cy="20" r="4" fill="currentColor"/>
      </g>
    </g>
    <g transform="translate(440,448)">
      <circle class="badge badge-light" r="41"/>
      <g class="glyph-dark">
        <rect x="-20" y="-20" width="14" height="5" fill="currentColor"/>
        <rect x="6" y="-20" width="14" height="5" fill="currentColor"/>
        <g fill="none" stroke="currentColor" stroke-width="2">
          <rect x="-9" y="-10" width="18" height="13"/>
          <rect x="-22" y="-10" width="8" height="16"/>
          <rect x="14" y="-10" width="8" height="16"/>
          <rect x="-26" y="8" width="52" height="8"/>
          <line x1="-22" y1="16" x2="-22" y2="20"/>
          <line x1="22" y1="16" x2="22" y2="20"/>
        </g>
      </g>
    </g>
    <g transform="translate(627,448)">
      <circle class="badge badge-accent" r="41"/>
      <g class="glyph-light" fill="currentColor">
        <rect x="-26" y="-14" width="14" height="28" rx="2"/>
        <rect x="12" y="-14" width="14" height="28" rx="2"/>
        <rect x="-9" y="0" width="18" height="14" rx="1"/>
        <rect x="-9" y="-7" width="18" height="5"/>
        <circle cx="-19" cy="-6" r="3" class="cut-accent"/>
        <circle cx="-19" cy="6" r="4.5" class="cut-accent"/>
        <circle cx="19" cy="-6" r="3" class="cut-accent"/>
        <circle cx="19" cy="6" r="4.5" class="cut-accent"/>
      </g>
    </g>
    <g transform="translate(815,448)">
      <circle class="badge badge-light" r="41"/>
      <g class="glyph-dark">
        <line x1="-10" y1="-24" x2="0" y2="-14" stroke="currentColor" stroke-width="2.5"/>
        <line x1="10" y1="-24" x2="0" y2="-14" stroke="currentColor" stroke-width="2.5"/>
        <rect x="-26" y="-14" width="52" height="36" rx="4" fill="currentColor"/>
        <rect x="-21" y="-9" width="34" height="26" rx="3" class="cut-white"/>
        <circle cx="20" cy="-3" r="2.5" class="cut-white"/>
        <circle cx="20" cy="6" r="2.5" class="cut-white"/>
      </g>
    </g>
    <g transform="translate(1008,448)">
      <circle class="badge badge-accent" r="41"/>
      <g class="glyph-light" fill="currentColor">
        <rect x="-2" y="-24" width="4" height="8"/>
        <path d="M-16 -2 A16 16 0 0 1 16 -2 Z"/>
        <rect x="-19" y="-2" width="38" height="4" rx="1"/>
        <circle cx="-14" cy="8" r="1.8"/><circle cx="-7" cy="8" r="1.8"/><circle cx="0" cy="8" r="1.8"/><circle cx="7" cy="8" r="1.8"/><circle cx="14" cy="8" r="1.8"/>
        <circle cx="-10" cy="14" r="1.8"/><circle cx="-3" cy="14" r="1.8"/><circle cx="4" cy="14" r="1.8"/><circle cx="11" cy="14" r="1.8"/>
        <circle cx="-7" cy="20" r="1.8"/><circle cx="0" cy="20" r="1.8"/><circle cx="7" cy="20" r="1.8"/>
      </g>
    </g>

    <!-- row three -->
    <g transform="translate(237,654)">
      <circle class="badge badge-light" r="41"/>
      <g class="glyph-dark" fill="none" stroke="currentColor" stroke-width="2.5">
        <ellipse cy="10" rx="26" ry="11"/>
        <ellipse cy="10" rx="18" ry="7.5"/>
        <ellipse cy="10" rx="10" ry="4"/>
        <path d="M-8 -4 q-4 -5 0 -9 q4 -5 0 -10"/>
        <path d="M0 -4 q-4 -5 0 -9 q4 -5 0 -10"/>
        <path d="M8 -4 q-4 -5 0 -9 q4 -5 0 -10"/>
      </g>
    </g>
    <g transform="translate(440,654)">
      <circle class="badge badge-accent" r="41"/>
      <g class="glyph-light">
        <g fill="none" stroke="currentColor" stroke-width="3">
          <rect x="-22" y="-24" width="44" height="48" rx="3"/>
          <line x1="-22" y1="-12" x2="22" y2="-12"/>
          <rect x="-15" y="-5" width="30" height="22"/>
          <line x1="-10" y1="10" x2="6" y2="-1" stroke-width="1.5"/>
        </g>
        <circle cx="-13" cy="-18" r="2" fill="currentColor"/>
        <circle cx="-5" cy="-18" r="2" fill="currentColor"/>
        <circle cx="13" cy="-18" r="2" fill="currentColor"/>
      </g>
    </g>
    <g transform="translate(627,654)">
      <circle class="badge badge-light" r="41"/>
      <g class="glyph-dark" fill="none" stroke="currentColor" stroke-width="2.5" stroke-linecap="round">
        <path d="M-6 8 V4 Q-14 -2 -14 -10 A14 14 0 0 1 14 -10 Q14 -2 6 4 V8 Z"/>
        <line x1="-6" y1="13" x2="6" y2="13"/>
        <line x1="-4" y1="18" x2="4" y2="18"/>
        <line x1="0" y1="-32" x2="0" y2="-28"/>
        <line x1="-22" y1="-22" x2="-19" y2="-19"/>
        <line x1="22" y1="-22" x2="19" y2="-19"/>
        <line x1="-28" y1="-8" x2="-23" y2="-8"/>
        <line x1="28" y1="-8" x2="23" y2="-8"/>
        <line x1="-22" y1="6" x2="-19" y2="3"/>
        <line x1="22" y1="6" x2="19" y2="3"/>
      </g>
    </g>
    <g transform="translate(815,654)">
      <circle class="badge badge-accent" r="41"/>
      <g class="glyph-light" fill="currentColor">
        <path d="M-26 -6 Q-26 -20 0 -20 Q26 -20 26 -6 L18 -2 L12 -10 H-12 L-18 -2 Z"/>
        <path d="M-14 -4 H14 L22 10 V20 H-22 V10 Z"/>
        <circle cx="-6" cy="4" r="1.8" class="cut-accent"/><circle cx="0" cy="4" r="1.8" class="cut-accent"/><circle cx="6" cy="4" r="1.8" class="cut-accent"/>
        <circle cx="-6" cy="10" r="1.8" class="cut-accent"/><circle cx="0" cy="10" r="1.8" class="cut-accent"/><circle cx="6" cy="10" r="1.8" class="cut-accent"/>
        <circle cx="-6" cy="16" r="1.8" class="cut-accent"/><circle cx="0" cy="16" r="1.8" class="cut-accent"/><circle cx="6" cy="16" r="1.8" class="cut-accent"/>
      </g>
    </g>
    <g transform="translate(1008,654)">
      <circle class="badge badge-light" r="41"/>
      <g class="glyph-dark" fill="currentColor">
        <path d="M-26 -6 L12 -18 L16 -8 L-22 4 Z"/>
        <path d="M-28 -4 L-24 6 L-20 4 L-24 -6 Z"/>
        <path d="M-10 2 L-6 10 L6 8 L4 -2 Z"/>
        <rect x="10" y="4" width="4" height="12"/>
        <rect x="14" y="-2" width="5" height="24" rx="1"/>
      </g>
    </g>
  </svg>

  <div class="service-label" style="left:237px; top:289px;">24 Hour<br>Emergency<br>Service</div>
  <div class="service-label" style="left:442px; top:289px;">New<br>Installations</div>
  <div class="service-label" style="left:626px; top:289px;">Repairs</div>
  <div class="service-label" style="left:814px; top:289px;">Maintenance</div>
  <div class="service-label" style="left:1009px; top:289px;">Renovations,<br>Extensions</div>

  <div class="service-label" style="left:238px; top:518px;">Re-Wiring</div>
  <div class="service-label" style="left:441px; top:516px;">Home<br>Theatre</div>
  <div class="service-label" style="left:629px; top:516px;">Surriund<br>Sound</div>
  <div class="service-label" style="left:816px; top:516px;">Wall Tv`s</div>
  <div class="service-label" style="left:1010px; top:516px;">Electric<br>Hot Water</div>

  <div class="service-label" style="left:237px; top:712px;">Stoves</div>
  <div class="service-label" style="left:439px; top:712px;">Cooktops</div>
  <div class="service-label" style="left:629px; top:712px;">Lighting,<br>Ceiling Fans</div>
  <div class="service-label" style="left:815px; top:712px;">Telephone</div>
  <div class="service-label" style="left:1010px; top:712px;">Security<br>Systems</div>

  <div class="bottom-band"></div>
</main>
</body>
</html>
```